Roof Plumbing Company needs simple, modern business card using the attached logo and below details:

Dean Halloway
Summit Gutters Pty Ltd
ABN: 58 214 937 062
Phone: 0417 286 531
Email: summitgutters@mailbrook.com
Website: summitgutters.com.au

For all of your metal roof plumbing requirements contact Summit Gutters for an obligation free quote - no job too big or to small!

Industry/Entity Type

Business

Contact Information for Business Card

Dean Halloway
Summit Gutters Pty Ltd
ABN 58 214 937 062
0417 286 531
summitgutters@mailbrook.com
summitgutters.com.au

Requirements
Must have
• Bright eye catching design, professional look

```html
<!DOCTYPE html>
<html lang="en">
<head>
<meta charset="utf-8">
<title>Summit Gutters – Business Card</title>
<link href="https://fonts.googleapis.com/css2?family=Montserrat:wght@500;600;700&display=swap" rel="stylesheet">
<style>
  :root {
    --page-bg: #dcd8d4;
    --card-white: #ffffff;
    --brand-red: #b81f26;
    --charcoal: #232323;
    --steel: #4a4a4a;
    --text-light: #ffffff;
  }
  * { box-sizing: border-box; margin: 0; padding: 0; }
  html, body {
    width: 1200px;
    height: 1000px;
    overflow: hidden;
    background: var(--page-bg);
    font-family: "Montserrat", Arial, sans-serif;
  }
  .canvas {
    width: 1200px;
    height: 1000px;
    display: flex;
    align-items: center;
    justify-content: center;
  }
  .business-card {
    width: 480px;
    height: 820px;
    display: flex;
    flex-direction: column;
    background: var(--card-white);
  }
  .brand-area {
    height: 294px;
    display: flex;
    flex-direction: column;
    align-items: center;
    justify-content: center;
    padding-top: 40px;
  }
  .brand-name {
    color: var(--brand-red);
    font-weight: 700;
    font-size: 40px;
    letter-spacing: 1px;
    line-height: 1.1;
    text-align: center;
    text-transform: uppercase;
  }
  .brand-name .brand-suffix {
    display: block;
    font-size: 40px;
  }
  .name-band {
    height: 115px;
    background: var(--brand-red);
    display: flex;
    align-items: center;
    justify-content: center;
  }
  .person-name {
    color: var(--text-light);
    font-weight: 500;
    font-size: 31px;
    text-transform: uppercase;
    letter-spacing: 0.5px;
  }
  .contact-area {
    flex: 1;
    background: var(--charcoal);
    border-top: 6px solid var(--steel);
    display: flex;
    flex-direction: column;
    align-items: center;
    justify-content: flex-end;
    padding-bottom: 52px;
  }
  .contact-list {
    list-style: none;
    display: flex;
    flex-direction: column;
    align-items: center;
    gap: 11px;
  }
  .contact-item {
    color: var(--text-light);
    font-size: 20px;
    font-weight: 500;
    display: flex;
    align-items: center;
    gap: 6px;
  }
  .contact-icon { width: 20px; height: 20px; flex: none; }
  .abn {
    margin-top: 28px;
    color: var(--text-light);
    font-size: 20px;
    font-weight: 500;
  }
</style>
</head>
<body>
<main class="canvas">
  <article class="business-card">
    <header class="brand-area">
      <p class="brand-name">Summit Gutters<span class="brand-suffix">Pty Ltd</span></p>
    </header>

    <section class="name-band">
      <h1 class="person-name">Dean Halloway</h1>
    </section>

    <section class="contact-area">
      <ul class="contact-list">
        <li class="contact-item">
          <svg class="contact-icon" viewBox="0 0 20 20" aria-hidden="true">
            <path d="M5 2 L8 6 L6.5 8 Q8.5 12 12 13.5 L14 12 L18 15 L16 18 Q8 18 3 10 Q2 5 5 2 Z" fill="#fff"/>
          </svg>
          0417 286 531
        </li>
        <li class="contact-item">
          <svg class="contact-icon" viewBox="0 0 20 20" aria-hidden="true">
            <rect x="2" y="5" width="16" height="11" fill="#fff"/>
            <path d="M2 5 L10 11 L18 5" fill="none" stroke="#232323" stroke-width="1.5"/>
          </svg>
          summitgutters@mailbrook.com
        </li>
        <li class="contact-item">
          <svg class="contact-icon" viewBox="0 0 20 20" aria-hidden="true">
            <circle cx="10" cy="10" r="9" fill="#fff"/>
            <path d="M5 6 L7.5 14 L10 8 L12.5 14 L15 6" fill="none" stroke="#232323" stroke-width="1.8" stroke-linejoin="round"/>
          </svg>
          summitgutters.com.au
        </li>
      </ul>
      <p class="abn">ABN 58 214 937 062</p>
    </section>
  </article>
</main>
</body>
</html>
```